Upgrade of Lumaro chocolate toffee design

Lumaro Choc toffee is a very popular sweet on the Zimbabwean market, we want to spruce up the design to make it more attractive. Attached is the existing design. The new design must be not more than six colours and for printing on photogravure which is a print technology for flexible packaging. The design should empahsise the chocolate flavour but we need to move away from the words rich and creamy. The design is aimed at the younger consumer and should look eyecatching

Target Market(s)

Middle income Zimbabwean consumers, mainly younger

Requirements
Must have
• Lumaro logo in the same format but with colour changes allowed. Also must have a clear window on the front of the pack through which the sweets can be seen

```html
<!DOCTYPE html>
<html lang="en">
<head>
<meta charset="utf-8">
<title>Lumaro Chocolate Toffees – Pack Front</title>
<link href="https://fonts.googleapis.com/css2?family=Cinzel:wght@400&family=Amatic+SC:wght@700&family=Playfair+Display:wght@400&display=swap" rel="stylesheet">
<style>
  :root {
    --pack-red: #7a0000;
    --panel-black: #000000;
    --trellis-tone: #2b2b27;
    --cream: #f3f1dc;
    --white: #ffffff;
    --toffee-light: #c98a2c;
    --toffee-mid: #8a4a08;
    --toffee-dark: #5e2f02;
    --page: #ffffff;
  }
  html, body {
    margin: 0;
    padding: 0;
    width: 1200px;
    height: 1200px;
    overflow: hidden;
    background: var(--page);
  }
  .canvas {
    display: block;
    width: 1200px;
    height: 1200px;
  }
  .pack-body { fill: var(--pack-red); }
  .hang-hole { fill: var(--white); }
  .trellis-field { fill: var(--trellis-tone); stroke: var(--cream); stroke-width: 5; }
  .title-banner { fill: var(--panel-black); stroke: var(--cream); stroke-width: 5; }
  .brand-name {
    font-family: "Cinzel", serif;
    font-size: 88px;
    fill: var(--white);
    letter-spacing: 2px;
  }
  .product-line {
    font-family: "Amatic SC", cursive;
    font-weight: 700;
    font-size: 50px;
    fill: var(--white);
  }
  .sweets-window { stroke: none; }
  .weight-badge { fill: var(--panel-black); stroke: var(--cream); stroke-width: 5; }
  .net-weight {
    font-family: "Playfair Display", serif;
    font-size: 72px;
    fill: var(--white);
  }
</style>
</head>
<body>
<svg class="canvas" viewBox="0 0 1500 1500" xmlns="http://www.w3.org/2000/svg">
  <defs>
    <linearGradient id="toffeeTone" x1="0" y1="0" x2="1" y2="1">
      <stop offset="0" stop-color="var(--toffee-light)"/>
      <stop offset="0.5" stop-color="var(--toffee-mid)"/>
      <stop offset="1" stop-color="var(--toffee-dark)"/>
    </linearGradient>
  </defs>

  <!-- pack -->
  <rect class="pack-body" x="360" y="20" width="762" height="1462"/>
  <rect class="hang-hole" x="652" y="58" width="153" height="42" rx="12"/>

  <!-- patterned field -->
  <polygon class="trellis-field" role="img" aria-label="Black and cream Moroccan trellis pattern"
    points="360,125 1122,125 1122,690 935,860 935,1482 548,1482 548,860 360,690"/>

  <!-- title banner -->
  <polygon class="title-banner" points="512,125 968,125 968,555 740,765 512,555"/>

  <text class="brand-name" x="745" y="462" text-anchor="middle">LUMARO</text>

  <text class="product-line" x="742" y="556" text-anchor="middle">CHOCOLATE TOFFEES</text>
  <text class="product-line" x="742" y="614" text-anchor="middle">GLUCOSE</text>
  <text class="product-line" x="742" y="671" text-anchor="middle">SWEETS</text>

  <!-- clear window showing the sweets -->
  <rect class="sweets-window" x="580" y="785" width="342" height="505" rx="30"
    fill="url(#toffeeTone)" role="img" aria-label="Three glossy chocolate toffee pieces seen through the pack window"/>

  <!-- weight badge -->
  <polygon class="weight-badge" points="605,1482 605,1372 740,1312 875,1372 875,1482"/>
  <text class="net-weight" x="740" y="1436" text-anchor="middle">75 G</text>
</svg>
</body>
</html>
```